Business Cards

Business cards (double-sided) to be handed out to clients and potential clients, with contact details, logo .

Target Market(s)

Small to medium size businesses

Industry/Entity Type

Accountants

Contact Information for Business Card

Brightwater Ledger & Counsel Ltd

Colors

Designer to choose only greyscale colors for use in the design.

Requirements
Must have
• Name, Title, Address, Phone number, Email, Website
Nice to have
• Modern, clean lines, classy
Should not have
• Business cards to be double-sided. Form keeps reverting to single-sided.

```html
<!DOCTYPE html>
<html lang="en">
<head>
<meta charset="utf-8">
<title>Brightwater Ledger &amp; Counsel – Business Card</title>
<link href="https://fonts.googleapis.com/css2?family=Montserrat:wght@300;400;700&display=swap" rel="stylesheet">
<style>
  :root {
    --backdrop: #d9d9db;
    --card: #232323;
    --card-edge: #1a1a1a;
    --ink-light: #f2f2f2;
    --ink-soft: #d6d6d6;
    --ink-emboss: #3a3a3a;
    --rule: #8a8a8a;
  }
  * { box-sizing: border-box; margin: 0; padding: 0; }
  html, body { width: 1200px; height: 961px; overflow: hidden; }
  body {
    background: var(--backdrop);
    font-family: "Montserrat", sans-serif;
    display: flex;
    flex-direction: column;
    align-items: center;
    justify-content: center;
    gap: 54px;
  }
  .card {
    width: 700px;
    height: 400px;
    border-radius: 36px;
    background: linear-gradient(160deg, #2c2c2c 0%, var(--card) 55%, var(--card-edge) 100%);
    box-shadow: 0 8px 22px rgba(0,0,0,.25);
    position: relative;
    overflow: hidden;
  }
  /* Back side */
  .card--back { display: flex; align-items: center; justify-content: center; }
  .card--back .brand-name {
    color: var(--ink-emboss);
    font-weight: 300;
    font-size: 34px;
    letter-spacing: 4px;
    text-align: center;
    line-height: 1.25;
  }
  /* Front side */
  .card--front { display: flex; align-items: center; }
  .card--front .brand {
    width: 350px;
    padding-left: 58px;
    display: flex;
    align-items: center;
    gap: 14px;
  }
  .brand-mark { width: 14px; height: 14px; background: var(--ink-light); flex: none; }
  .card--front .brand-name {
    color: var(--ink-light);
    font-weight: 300;
    font-size: 22px;
    letter-spacing: 2.5px;
    line-height: 1.3;
  }
  .divider { width: 1px; height: 236px; background: var(--rule); }
  .details { padding-left: 34px; color: var(--ink-soft); font-size: 17px; line-height: 1.45; }
  .details .person { color: #fff; font-weight: 700; font-size: 28px; letter-spacing: .5px; line-height: 1.2; }
  .details .role { margin-bottom: 6px; }
  .contact-line { display: flex; align-items: center; gap: 10px; }
  .contact-line svg { width: 15px; height: 15px; flex: none; fill: none; stroke: var(--ink-soft); stroke-width: 2; }
  .address { margin-top: 6px; }
</style>
</head>
<body>
  <section class="card card--back" aria-label="Card back">
    <p class="brand-name">BRIGHTWATER<br>LEDGER &amp; COUNSEL</p>
  </section>

  <section class="card card--front" aria-label="Card front">
    <div class="brand">
      <span class="brand-mark"></span>
      <p class="brand-name">BRIGHTWATER<br>LEDGER &amp; COUNSEL</p>
    </div>
    <div class="divider"></div>
    <div class="details">
      <p class="person">ADRIAN HALE</p>
      <p class="role">Managing Director</p>
      <p class="contact-line">
        <svg viewBox="0 0 24 24"><path d="M5 3h4l2 5-3 2a12 12 0 0 0 6 6l2-3 5 2v4a2 2 0 0 1-2 2A18 18 0 0 1 3 5a2 2 0 0 1 2-2z"/></svg>
        000-000-0000
      </p>
      <p class="contact-line">
        <svg viewBox="0 0 24 24"><rect x="3" y="5" width="18" height="14"/><path d="M3 5l9 8 9-8"/></svg>
        Youremail@email.com
      </p>
      <p class="contact-line">
        <svg viewBox="0 0 24 24"><circle cx="12" cy="12" r="9"/><path d="M3 12h18M12 3c3 3 3 15 0 18M12 3c-3 3-3 15 0 18"/></svg>
        Your webadress here
      </p>
      <p class="address">421, Address line here<br>Country Name, 45452</p>
    </div>
  </section>
</body>
</html>
```